Etiketten-Design für Honig
Zielgruppe
Selbst: Imker
Zielgruppe: Privatkunden/ Verbraucher
Aufgabenstellung
Ich verkaufe Honig. Design soll hip sein. Auf dem Logo soll mein Name meine Anschrift stehen, aber nicht dominant. Es muss ersichtlich sein, dass es Honig ist, der verkauft wird. Ideal wäre, wenn zum Ankreuzen je ein Feld mit der Bezeichnung Waldhonig bzw. Blütenhonig stünde.
Ich benötige ein Lehrfeld mit der Kennzeichnung „Mindestens haltbar bis“
Gewichtsangabe Fixfeld mit 500 g.
Format: ca.9,5 x 5,5 cm

```html
<!DOCTYPE html>
<html lang="de">
<head>
<meta charset="utf-8">
<title>Honig Etikett</title>
<link rel="stylesheet" href="https://fonts.googleapis.com/css2?family=Montserrat:wght@400;700&display=swap">
<style>
  :root {
    --page-bg: #e7e5e6;
    --label-mint: #afd0cc;
    --honey: #f4a82a;
    --honey-tint: #f2c27a;
    --field-white: #ffffff;
    --ink-taupe: #8a7d78;
    --text-white: #ffffff;
  }
  * { margin: 0; padding: 0; box-sizing: border-box; }
  html, body {
    width: 1200px;
    height: 1107px;
    overflow: hidden;
    background: var(--page-bg);
    font-family: "Montserrat", Arial, sans-serif;
  }
  .label {
    position: absolute;
    left: 50px;
    top: 236px;
    width: 1100px;
    height: 635px;
    display: block;
  }
  .label-base { fill: var(--label-mint); }
  .bee-decoration { fill: url(#beeGlow); }
  .bee-icon { fill: var(--honey-tint); opacity: 0.55; }
  .product-name { font-family: "Montserrat", Arial, sans-serif; font-weight: 700; font-size: 112px; fill: var(--honey); }
  .tick-box { fill: none; stroke: var(--honey); stroke-width: 3; }
  .variety { font-family: "Montserrat", Arial, sans-serif; font-weight: 700; font-size: 21px; fill: var(--text-white); letter-spacing: 1px; }
  .weight { font-family: "Montserrat", Arial, sans-serif; font-weight: 700; font-size: 30px; fill: var(--honey); }
  .weight-unit { font-size: 24px; }
  .bbd-field { fill: var(--field-white); }
  .bbd-text { font-family: "Montserrat", Arial, sans-serif; font-weight: 400; font-size: 16px; fill: var(--ink-taupe); }
  .producer { font-family: "Montserrat", Arial, sans-serif; font-size: 16.5px; fill: var(--ink-taupe); }
  .producer-name { font-weight: 700; }
  .producer-address { font-weight: 400; }
</style>
</head>
<body>
<svg class="label" viewBox="0 0 800 462" xmlns="http://www.w3.org/2000/svg">
  <defs>
    <radialGradient id="beeGlow" cx="0.5" cy="0.5" r="0.5">
      <stop offset="0" stop-color="#c9e0dc" stop-opacity="0.55"/>
      <stop offset="1" stop-color="#c9e0dc" stop-opacity="0"/>
    </radialGradient>
  </defs>

  <rect class="label-base" x="0" y="0" width="800" height="462"/>

  <rect class="bee-decoration" x="30" y="0" width="690" height="462" role="img" aria-label="Große, feine Bienen-Umrisszeichnung als Hintergrunddekor"/>

  <rect class="bee-icon" x="554" y="34" width="98" height="80" rx="6" role="img" aria-label="Kleine Bienen-Illustration in Honiggelb"/>

  <text class="product-name" x="194" y="216" textLength="415" lengthAdjust="spacing">HONIG</text>

  <g class="varieties">
    <polygon class="tick-box" points="208,237 217,242 217,252 208,257 199,252 199,242"/>
    <text class="variety" x="230" y="255">WALDHONIG</text>
    <polygon class="tick-box" points="208,274 217,279 217,289 208,294 199,289 199,279"/>
    <text class="variety" x="230" y="293">BLÜTENHONIG</text>
  </g>

  <text class="weight" x="396" y="439" text-anchor="middle">500 <tspan class="weight-unit">g</tspan></text>

  <rect class="bbd-field" x="716" y="210" width="84" height="252"/>
  <text class="bbd-text" transform="translate(738 449) rotate(-90)">Mindestens haltbar bis:</text>

  <g class="producer">
    <text transform="translate(47 441) rotate(-90)"><tspan class="producer-name">Hersteller: Vorame Zuname</tspan><tspan class="producer-address">,</tspan></text>
    <text class="producer-address" transform="translate(66 441) rotate(-90)">Musterstr. 55, 754876 Musterstadt.</text>
  </g>
</svg>
</body>
</html>
```